Pixor Ad Design for Culinary Toursim Company

Looking for ad design for www.savorlanewalks.example to be used on PIXOR traffic ads.

Below is one example of the

We are looking for pixor ad design
Post: 1080x1080 with text,
Stories: 1080x1920 with text

Text should read
Food For Thought
CTA: Join our {CITY} Food Tour

Logo and optional photos are attached. You can edit the photos as you see fit.
Brand guidelines https://files.bramblevault.example/share/Savor-Lane-Walks-Brand-Guidelines.docx

Logos https://files.bramblevault.example/share/savor-lane-logos

Target Market(s)

United States Foodies ages 30-65

Industry/Entity Type

Tourism

Font styles to use
Other font styles liked:
• Avenir

Requirements
Must have
• High Design
Nice to have
• See Brand Guidelines
Should not have
• See Brand Guidelines

```html
<!DOCTYPE html>
<html lang="en">
<head>
<meta charset="utf-8">
<title>Savor Lane Walks – Food For Thought Ad Set</title>
<link rel="stylesheet" href="https://fonts.googleapis.com/css2?family=DM+Sans:wght@400;500;600;700&display=swap">
<style>
  :root {
    --brand-red: #b40000;
    --ink: #000000;
    --paper: #ffffff;
    --backdrop: #e6e6e6;
    --tile-blue: #3467b3;
    --tile-teal: #2f9c97;
    --tile-yellow: #f8b84a;
  }
  * { margin: 0; padding: 0; box-sizing: border-box; }
  html, body { width: 1200px; height: 811px; overflow: hidden; }
  body {
    background: var(--backdrop);
    font-family: "DM Sans", "Avenir", sans-serif;
    position: relative;
  }
  .ad {
    position: absolute;
    width: 350px;
    height: 350px;
    overflow: hidden;
  }
  .ad--athens   { left: 42px;  top: 39px;  background: var(--brand-red); }
  .ad--la       { left: 425px; top: 39px;  background: var(--paper); }
  .ad--istanbul { left: 808px; top: 39px;  background: var(--ink); }
  .ad--cities   { left: 42px;  top: 421px; background: var(--brand-red); }
  .ad--naples   { left: 425px; top: 421px; background: #3a2b26; }
  .ad--market   { left: 808px; top: 421px; background: var(--brand-red); }

  .ad__shapes { position: absolute; inset: 0; width: 350px; height: 350px; }

  .headline {
    position: absolute;
    font-weight: 600;
    color: var(--paper);
    letter-spacing: -0.2px;
  }
  .headline--stack { left: 27px; font-size: 29px; line-height: 32px; }
  .headline--red { color: var(--brand-red); font-size: 31px; line-height: 38px; }
  .headline--center {
    left: 0; right: 0; text-align: center;
    font-size: 27px; line-height: 30px;
  }
  .cta {
    position: absolute;
    color: var(--paper);
    font-weight: 400;
    font-size: 15.5px;
    line-height: 22px;
  }
  .cta--stack { left: 27px; }
  .cta--center { left: 0; right: 0; text-align: center; }
  .cta--bubble {
    left: 241px; top: 187px; width: 102px;
    text-align: center; font-size: 12px; line-height: 17.5px;
  }

  .site {
    position: absolute;
    left: 27px;
    display: flex;
    align-items: center;
    gap: 8px;
    color: var(--paper);
    font-size: 8px;
    font-weight: 600;
    letter-spacing: 0.2px;
  }
  .site svg { width: 11px; height: 11px; }

  .brand-name {
    position: absolute;
    font-size: 10px;
    font-weight: 600;
    letter-spacing: 0.3px;
    white-space: nowrap;
  }
  .brand-name--dark { color: var(--ink); }
  .brand-name--light { color: var(--paper); }

  .city-tile {
    position: absolute;
    top: 212px;
    width: 83px;
    height: 83px;
    border-radius: 9px;
    color: var(--paper);
    font-size: 9.5px;
    font-weight: 500;
    letter-spacing: -0.2px;
    display: flex;
    align-items: flex-end;
    justify-content: center;
    padding-bottom: 17px;
  }
  .city-tile--athens { left: 45px;  background: var(--tile-blue); }
  .city-tile--lisbon { left: 134px; background: var(--tile-teal); }
  .city-tile--oaxaca { left: 223px; background: var(--tile-yellow); }
</style>
</head>
<body>

<!-- Athens post -->
<section class="ad ad--athens">
  <svg class="ad__shapes" viewBox="0 0 350 350">
    <defs>
      <linearGradient id="athensPhoto" x1="0" y1="0" x2="1" y2="1">
        <stop offset="0" stop-color="#8b6f55"/>
        <stop offset="0.45" stop-color="#3f6b3a"/>
        <stop offset="1" stop-color="#5d5a57"/>
      </linearGradient>
    </defs>
    <path d="M160,0 C150,30 175,45 215,55 C260,65 250,95 290,110 C330,125 320,160 350,175 L350,0 Z" fill="var(--paper)"/>
    <path role="img" aria-label="Photo: local cook in a green blouse sorting chickpeas in a colander"
          d="M0,155 L55,155 C85,160 120,175 150,200 C190,235 230,230 280,245 C330,262 325,300 320,350 L0,350 Z"
          fill="url(#athensPhoto)"/>
    <circle cx="292" cy="216" r="51" fill="var(--ink)"/>
  </svg>
  <span class="brand-name brand-name--dark" style="left:252px; top:78px;">Savor Lane Walks</span>
  <h2 class="headline headline--stack" style="top:40px; line-height:42px;">Food<br>For Thought</h2>
  <p class="cta cta--bubble">Join our<br>Athen<br>Food Tour</p>
  <div class="site" style="top:317px;">
    <svg viewBox="0 0 12 12" fill="none" stroke="currentColor" stroke-width="1"><circle cx="6" cy="6" r="5.2"/><ellipse cx="6" cy="6" rx="2.3" ry="5.2"/><path d="M0.8 6h10.4M1.6 3.4h8.8M1.6 8.6h8.8"/></svg>
    savorlanewalks.example
  </div>
</section>

<!-- Los Angeles post -->
<section class="ad ad--la">
  <svg class="ad__shapes" viewBox="0 0 350 350">
    <defs>
      <radialGradient id="laPhoto" cx="0.45" cy="0.55" r="0.7">
        <stop offset="0" stop-color="#a07a52"/>
        <stop offset="0.6" stop-color="#4e3b2c"/>
        <stop offset="1" stop-color="#2a211b"/>
      </radialGradient>
    </defs>
    <path d="M116,0 C110,40 125,75 175,70 C220,65 260,50 290,60 C320,70 335,70 350,65 L350,0 Z" fill="var(--brand-red)"/>
    <circle role="img" aria-label="Photo: chef plating dishes at a restaurant kitchen counter"
            cx="262" cy="163" r="112" fill="url(#laPhoto)"/>
    <path d="M0,212 C60,200 140,205 170,220 C200,240 175,290 190,320 C200,340 220,345 235,350 L0,350 Z" fill="var(--ink)"/>
  </svg>
  <span class="brand-name brand-name--dark" style="left:27px; top:50px;">Savor Lane Walks</span>
  <h2 class="headline headline--stack headline--red" style="top:84px;">Food<br>For<br>Thought</h2>
  <p class="cta cta--stack" style="top:222px;">Join our<br>Los Angeles<br>Food Tour</p>
  <div class="site" style="top:306px;">
    <svg viewBox="0 0 12 12" fill="none" stroke="currentColor" stroke-width="1"><circle cx="6" cy="6" r="5.2"/><ellipse cx="6" cy="6" rx="2.3" ry="5.2"/><path d="M0.8 6h10.4M1.6 3.4h8.8M1.6 8.6h8.8"/></svg>
    savorlanewalks.example
  </div>
</section>

<!-- Istanbul post, black -->
<section class="ad ad--istanbul">
  <svg class="ad__shapes" viewBox="0 0 350 350">
    <defs>
      <linearGradient id="istanbulPhoto" x1="0" y1="0" x2="1" y2="1">
        <stop offset="0" stop-color="#b9a58c"/>
        <stop offset="0.5" stop-color="#e6e2dc"/>
        <stop offset="1" stop-color="#6e4a35"/>
      </linearGradient>
    </defs>
    <path d="M111,0 C130,25 160,45 195,35 C225,25 240,10 260,0 Z" fill="var(--brand-red)"/>
    <path role="img" aria-label="Photo: chef in white coat pouring a drink in front of tiled wall"
          d="M215,55 C250,40 300,38 350,37 L350,285 C300,282 270,292 235,282 C180,272 155,245 155,205 C155,150 170,90 215,55 Z"
          fill="url(#istanbulPhoto)"/>
    <path d="M0,272 C50,255 110,265 160,292 C200,315 240,320 270,330 C285,338 295,345 305,350 L0,350 Z" fill="var(--brand-red)"/>
  </svg>
  <span class="brand-name brand-name--light" style="left:27px; top:34px;">Savor Lane Walks</span>
  <h2 class="headline headline--stack" style="top:80px;">Food<br>For<br>Thought</h2>
  <p class="cta cta--stack" style="top:187px;">Join our<br>Istanbul<br>Food Tour</p>
  <div class="site" style="top:306px;">
    <svg viewBox="0 0 12 12" fill="none" stroke="currentColor" stroke-width="1"><circle cx="6" cy="6" r="5.2"/><ellipse cx="6" cy="6" rx="2.3" ry="5.2"/><path d="M0.8 6h10.4M1.6 3.4h8.8M1.6 8.6h8.8"/></svg>
    savorlanewalks.example
  </div>
</section>

<!-- Multi-city post -->
<section class="ad ad--cities">
  <svg class="ad__shapes" viewBox="0 0 350 350">
    <defs>
      <linearGradient id="citiesPhoto" x1="0" y1="0" x2="0" y2="1">
        <stop offset="0" stop-color="#4a3d33"/>
        <stop offset="0.6" stop-color="#6b5443"/>
        <stop offset="1" stop-color="#3a3f57"/>
      </linearGradient>
    </defs>
    <rect role="img" aria-label="Photo: smiling cook leaning on a kitchen counter under pendant lamps"
          x="0" y="0" width="350" height="350" fill="url(#citiesPhoto)"/>
    <path d="M0,162 C50,158 100,170 125,200 C150,225 215,225 245,200 C270,175 310,160 350,158 L350,350 L0,350 Z" fill="var(--brand-red)"/>
  </svg>
  <h2 class="headline headline--center" style="top:147px;">Food For Thought</h2>
  <p class="cta cta--center" style="top:179px;">Join our Food Tour</p>
  <div class="city-tile city-tile--athens">ATHENS</div>
  <div class="city-tile city-tile--lisbon">LISBON</div>
  <div class="city-tile city-tile--oaxaca">OAXACA</div>
  <div class="site" style="top:321px;">
    <svg viewBox="0 0 12 12" fill="none" stroke="currentColor" stroke-width="1"><circle cx="6" cy="6" r="5.2"/><ellipse cx="6" cy="6" rx="2.3" ry="5.2"/><path d="M0.8 6h10.4M1.6 3.4h8.8M1.6 8.6h8.8"/></svg>
    savorlanewalks.example
  </div>
</section>

<!-- Naples post -->
<section class="ad ad--naples">
  <svg class="ad__shapes" viewBox="0 0 350 350">
    <defs>
      <linearGradient id="naplesPhoto" x1="0" y1="0" x2="0" y2="1">
        <stop offset="0" stop-color="#6b4b4f"/>
        <stop offset="0.5" stop-color="#7a4a32"/>
        <stop offset="1" stop-color="#3b3a26"/>
      </linearGradient>
    </defs>
    <rect role="img" aria-label="Photo: vendor at a pickle and spice stall lined with jars"
          x="0" y="0" width="350" height="350" fill="url(#naplesPhoto)"/>
    <rect x="0" y="0" width="350" height="350" fill="#000" opacity="0.25"/>
    <path d="M0,270 C40,255 90,265 120,285 C160,310 200,310 230,325 C245,333 250,345 255,350 L0,350 Z" fill="var(--brand-red)"/>
  </svg>
  <h2 class="headline headline--center" style="top:178px;">Food For Thought</h2>
  <p class="cta cta--center" style="top:211px;">Join our<br>Naples Food Tour</p>
  <span class="brand-name brand-name--light" style="left:252px; top:290px;">Savor Lane Walks</span>
  <div class="site" style="top:318px; left:17px;">
    <svg viewBox="0 0 12 12" fill="none" stroke="currentColor" stroke-width="1"><circle cx="6" cy="6" r="5.2"/><ellipse cx="6" cy="6" rx="2.3" ry="5.2"/><path d="M0.8 6h10.4M1.6 3.4h8.8M1.6 8.6h8.8"/></svg>
    savorlanewalks.example
  </div>
</section>

<!-- Market post -->
<section class="ad ad--market">
  <svg class="ad__shapes" viewBox="0 0 350 350">
    <defs>
      <linearGradient id="marketPhoto" x1="0" y1="0" x2="1" y2="1">
        <stop offset="0" stop-color="#4f8a3a"/>
        <stop offset="0.5" stop-color="#d59a3a"/>
        <stop offset="1" stop-color="#c13a2a"/>
      </linearGradient>
    </defs>
    <path role="img" aria-label="Photo: smiling vendor holding a pepper at a fruit and vegetable market"
          d="M80,0 C95,40 130,70 175,90 C215,108 240,100 260,130 C280,160 300,185 350,190 L350,0 Z"
          fill="url(#marketPhoto)"/>
    <path d="M350,205 C310,210 290,230 270,265 C250,300 200,310 155,350 L350,350 Z" fill="var(--ink)"/>
  </svg>
  <span class="brand-name brand-name--light" style="left:27px; top:62px;">Savor Lane Walks</span>
  <h2 class="headline headline--stack" style="top:131px;">Food<br>For Thought</h2>
  <p class="cta cta--stack" style="top:212px;">Join our<br>Istanbul<br>Food Tour</p>
  <div class="site" style="top:318px;">
    <svg viewBox="0 0 12 12" fill="none" stroke="currentColor" stroke-width="1"><circle cx="6" cy="6" r="5.2"/><ellipse cx="6" cy="6" rx="2.3" ry="5.2"/><path d="M0.8 6h10.4M1.6 3.4h8.8M1.6 8.6h8.8"/></svg>
    savorlanewalks.example
  </div>
</section>

</body>
</html>
```